VELDA Motorcycle Ad

We import a range of specialised high end competition Off-Road motorcycles from Spain. We have a new model out called the VELDA Kx340e which we would like a banner ad for. The main features we want to highlight on the new VELDA is the light weight (lightest on the market) BRAKMOR rear shock (Best on the market) & an industry leading 2 year warranty. We can supply images etc. tis is our first time using this service so not sure of the procedure.

```html
<!DOCTYPE html>
<html lang="en">
<head>
<meta charset="utf-8">
<title>VELDA Kx340e banner</title>
<link href="https://fonts.googleapis.com/css2?family=Raleway:wght@200&family=Roboto:wght@400&display=swap" rel="stylesheet">
<style>
  :root {
    --bg: #050505;
    --bg-edge: #1a1a1a;
    --panel: #ffffff;
    --green: #8cc63f;
    --white: #ffffff;
    --ink: #1a1a1a;
    --mesh-light: #6e6e6e;
    --mesh-dark: #1c1c1c;
    --bike-light: #8a8a8a;
    --bike-dark: #d8d8d8;
  }
  html, body {
    margin: 0;
    padding: 0;
    width: 1200px;
    height: 148px;
    overflow: hidden;
    background: var(--panel);
  }
  .banner {
    position: relative;
    width: 1200px;
    height: 148px;
    overflow: hidden;
    background: var(--panel);
    font-family: "Roboto", Arial, sans-serif;
  }
  .dark-panel {
    position: absolute;
    left: 0;
    top: 0;
    width: 778px;
    height: 148px;
    background: linear-gradient(180deg, var(--bg) 0%, var(--bg) 75%, var(--bg-edge) 100%);
  }
  .mesh-decoration {
    position: absolute;
    left: 0;
    top: 80px;
    width: 290px;
    height: 68px;
    background: radial-gradient(ellipse at 30% 100%, var(--mesh-light) 0%, var(--mesh-dark) 60%, transparent 85%);
    opacity: 0.8;
  }
  .headline {
    position: absolute;
    left: 34px;
    top: 0;
    margin: 0;
    font-family: "Raleway", "Helvetica Neue", sans-serif;
    font-weight: 200;
    font-size: 94px;
    line-height: 1;
    letter-spacing: -1px;
    color: var(--green);
  }
  .features {
    position: absolute;
    left: 540px;
    top: 26px;
    margin: 0;
    padding: 0;
    list-style: none;
    color: var(--white);
    font-size: 22px;
    line-height: 32px;
  }
  .bike {
    position: absolute;
    border-radius: 30px;
    background: radial-gradient(ellipse at 50% 55%, var(--bike-light) 0%, var(--bike-dark) 75%, transparent 100%);
  }
  .bike--left { left: 806px; top: 40px; width: 110px; height: 96px; }
  .bike--right { left: 918px; top: 14px; width: 112px; height: 124px; }
  .brand {
    position: absolute;
    left: 1050px;
    top: 54px;
    display: flex;
    align-items: center;
    gap: 8px;
    color: var(--ink);
    font-size: 30px;
    font-weight: 400;
    letter-spacing: 1px;
  }
  .brand-dot {
    width: 16px;
    height: 16px;
    border-radius: 50%;
    background: var(--green);
  }
</style>
</head>
<body>
  <div class="banner">
    <div class="dark-panel"></div>
    <div class="mesh-decoration" role="img" aria-label="Curved grey wireframe mesh decoration"></div>
    <h1 class="headline">lightweight</h1>
    <ul class="features">
      <li>BRAKMOR rear shock</li>
      <li>2 year warranty</li>
    </ul>
    <div class="bike bike--left" role="img" aria-label="Photo of the VELDA Kx340e trial motorcycle, side view"></div>
    <div class="bike bike--right" role="img" aria-label="Photo of the VELDA Kx340e motorcycle, front three-quarter view"></div>
    <div class="brand">
      <span class="brand-dot"></span>
      <span class="brand-name">VELDA</span>
    </div>
  </div>
</body>
</html>
```